Poster for Starlette-style Christmas music and dance show.

I need a poster for a Christmas music and dance show styled after the Harbor Lane Starlettes. Attached are samples of posters for previous years. I like the font style and colors of the blue one. The design should contain an ornament design with dancers dancing on it. The dancers should be cartoon style, not photo real. A sample is attached.
The poster MUST contain the PelMUSE logo, sponsor logos, the dates (December 12-13, 2015), the location (Lyle & Ruth Danvers Theatre, 4817 Quillberry Bend, Cedarholt, NV), PelMUSE contact info (www.pel-muse.example and 555-307-4162 ext 204), and "Directed and Choreographed by Colin Ashby."
Logos are all attached. Finalized files needed in sizes: 12x18, 4x6, and 30x48 inches.

Target Market(s)

Community Theatre patrons

Industry/Entity Type

Radio

Font styles to use
Serif

Colors
0792cd
33a6d7
85cae6
ecf7fb
ffffff

Requirements
Must have
• PelMUSE logo (attached)
• sponsor logos: Neva Orr Photography, Pruitt Dentistry, Bluefin Grill, Up Tempo (attached)
• Show dates: December 12-13, 2015)
• Show Location: Lyle & Ruth Danvers Theatre, 4817 Quillberry Bend, Cedarholt, NV)
• PelMUSE contact info: www.pel-muse.example and 555-307-4162 ext 204
• "Directed and Choreographed by Colin Ashby"
• An ornament design with dancers on it. The dancers should be cartoon style, not photo real. A sample of a dancer graphic is attached.
Nice to have
• snowflakes or other winter themes

```html
<!DOCTYPE html>
<html lang="en">
<head>
<meta charset="utf-8">
<title>The Holiday Extravaganza – PelMUSE</title>
<link rel="stylesheet" href="https://fonts.googleapis.com/css2?family=Yellowtail&family=Raleway:wght@700;800&family=Lora:wght@600&display=swap">
<style>
  :root {
    --blue-deep: #0792cd;
    --blue-mid: #33a6d7;
    --blue-soft: #85cae6;
    --blue-mist: #ecf7fb;
    --white: #ffffff;
    --ink: #1d2b36;
    --silver: #c9d3da;
  }
  * { margin: 0; padding: 0; box-sizing: border-box; }
  html, body { width: 800px; height: 1200px; overflow: hidden; background: var(--white); }
  .poster {
    position: relative;
    width: 800px;
    height: 1200px;
    overflow: hidden;
    background:
      radial-gradient(ellipse 70% 45% at 50% 42%, var(--white) 0%, rgba(255,255,255,0) 75%),
      radial-gradient(circle at 88% 12%, rgba(255,255,255,0.95) 0 40px, rgba(255,255,255,0) 120px),
      radial-gradient(circle at 10% 30%, rgba(255,255,255,0.9) 0 30px, rgba(255,255,255,0) 100px),
      linear-gradient(180deg, #dfe6eb 0%, var(--blue-mist) 45%, #e4eaee 100%);
    font-family: "Raleway", sans-serif;
    color: var(--ink);
    text-align: center;
  }
  .poster > * { position: absolute; left: 0; right: 0; white-space: nowrap; }
  .poster__frame {
    inset: 14px;
    border: 3px solid var(--blue-soft);
    pointer-events: none;
  }
  .ornament-backdrop {
    left: auto; right: auto;
    border-radius: 50%;
    background: radial-gradient(circle at 35% 30%, #ffffff 0%, var(--silver) 55%, #aab6bf 100%);
    opacity: 0.55;
  }
  .ornament-backdrop--left { left: -80px; top: 330px; width: 260px; height: 260px; }
  .ornament-backdrop--right { left: 440px; top: 560px; width: 330px; height: 330px; }
  .ornament-backdrop--top { left: 470px; top: 250px; width: 150px; height: 150px; opacity: 0.4; }

  .presenter {
    top: 30px; line-height: 60px;
    font-family: "Lora", serif; font-weight: 600;
    font-size: 50px; color: var(--blue-deep);
  }
  .presents {
    top: 95px; line-height: 50px;
    font-family: "Yellowtail", cursive; font-size: 40px;
    color: var(--ink);
  }
  .title__the {
    top: 205px; left: 110px; right: auto; line-height: 60px;
    font-family: "Yellowtail", cursive; font-size: 54px;
    color: var(--blue-deep);
  }
  .title__main {
    top: 235px; line-height: 180px;
    font-family: "Yellowtail", cursive; font-weight: 400; font-size: 170px;
    color: var(--blue-mid);
    text-shadow: 3px 3px 0 var(--white), 0 6px 14px rgba(7,146,205,0.25);
  }
  .title__sub {
    top: 420px; left: 200px; line-height: 46px;
    font-weight: 700; font-size: 36px; letter-spacing: 1px;
    color: var(--blue-mid);
  }
  .dancers {
    left: 240px; right: auto; top: 520px;
    width: 310px; height: 175px;
    border-radius: 12px;
    background: linear-gradient(180deg, var(--blue-soft) 0%, var(--blue-mid) 100%);
    opacity: 0.85;
  }
  .credit__label {
    top: 705px; line-height: 40px;
    font-family: "Yellowtail", cursive; font-size: 34px; color: var(--ink);
  }
  .credit__name {
    top: 752px; line-height: 44px;
    font-weight: 700; font-size: 36px; letter-spacing: 1px;
    color: var(--blue-deep);
  }
  .dates {
    top: 830px; line-height: 80px;
    font-family: "Yellowtail", cursive; font-size: 72px;
    color: var(--blue-deep);
  }
  .venue__name {
    top: 925px; line-height: 30px;
    font-weight: 800; font-size: 22px; letter-spacing: 0.5px;
    text-transform: uppercase; color: var(--ink);
  }
  .venue__details {
    top: 957px; line-height: 20px;
    font-weight: 700; font-size: 13px; letter-spacing: 0.3px;
    text-transform: uppercase; color: var(--ink);
  }
  .sponsors {
    left: 40px; right: 40px; top: 1030px; height: 60px;
    display: flex; justify-content: space-between; align-items: center;
  }
  .sponsor {
    display: flex; align-items: center; gap: 8px;
    font-weight: 700; font-size: 19px; color: var(--ink);
  }
  .sponsor__mark { width: 18px; height: 18px; border-radius: 50%; background: var(--blue-mid); }
  .sponsor__mark--square { border-radius: 0; background: var(--ink); }
</style>
</head>
<body>
<main class="poster">
  <div class="ornament-backdrop ornament-backdrop--left" role="img" aria-label="Soft silver holiday ornament in the background"></div>
  <div class="ornament-backdrop ornament-backdrop--top" role="img" aria-label="Small hanging silver ornament"></div>
  <div class="ornament-backdrop ornament-backdrop--right" role="img" aria-label="Large silver holiday ornament in the background"></div>
  <div class="poster__frame"></div>

  <p class="presenter">PelMUSE</p>
  <p class="presents">presents</p>

  <span class="title__the">The</span>
  <h1 class="title__main">Holiday</h1>
  <p class="title__sub">EXTRAVAGANZA</p>

  <div class="dancers" role="img" aria-label="Four cartoon Starlette-style dancers kicking in a line, in blue silhouette"></div>

  <p class="credit__label">Directed and Choreographed by</p>
  <p class="credit__name">COLIN ASHBY</p>

  <p class="dates">December 12-13, 2015</p>

  <p class="venue__name">Lyle &amp; Ruth Danvers Theatre</p>
  <p class="venue__details">4817 Quillberry Bend, Cedarholt, NV &bull; www.pel-muse.example &bull; 555-307-4162 ext 204</p>

  <div class="sponsors">
    <span class="sponsor"><span class="sponsor__mark"></span>Neva Orr Photography</span>
    <span class="sponsor">Pruitt Dentistry</span>
    <span class="sponsor"><span class="sponsor__mark sponsor__mark--square"></span>Bluefin Grill</span>
    <span class="sponsor">Up Tempo</span>
  </div>
</main>
</body>
</html>
```